cargo van wrap for home buildedr

New service van wrap. its a corvane b370 I will attach the templet for correct sizing in the link https://files.plumvexa.net/share/8rtWqLm2Zy4nHdKp0sXbVfJ7aE3uQc6Gi/view?usp=link_src_b&invite=TRmXoPa&ts=71940265
we are a custom home builder in lees summit mo
the black and gold log we have home pictures we can put into vans
i will send pics of some of our other trucks and logo does not need to look like the old ones just for reference

Target Market(s)

home buyers

Industry/Entity Type

home builder

Font styles to use
Sans Serif

Requirements
Must have
• picture of home and logo

```html
<!DOCTYPE html>
<html lang="en">
<head>
<meta charset="UTF-8">
<title>Brantley Construction – Service Van Wrap</title>
<link rel="stylesheet" href="https://fonts.googleapis.com/css2?family=Montserrat:wght@500;600;700&display=swap">
<style>
  :root {
    --canvas: #ffffff;
    --wrap-black: #050505;
    --gold: #d9c48f;
    --gold-deep: #c9b27a;
    --gold-light: #ece0b8;
    --photo-green: #2f4a33;
    --photo-wood: #9a6a3c;
    --photo-sky: #4a5560;
    --ink: #0a0a0a;
  }
  * { margin: 0; padding: 0; box-sizing: border-box; }
  html, body {
    width: 1200px;
    height: 922px;
    overflow: hidden;
    background: var(--canvas);
    font-family: "Montserrat", Arial, sans-serif;
  }
  .wrap-panel {
    position: absolute;
    left: 100px;
    top: 245px;
    width: 1010px;
    height: 370px;
    background: var(--wrap-black);
    border-radius: 40px 120px 30px 20px;
    overflow: hidden;
  }
  .home-photo {
    position: absolute;
    left: 0;
    top: 0;
    width: 420px;
    height: 100%;
    background:
      linear-gradient(90deg, rgba(5,5,5,0) 0%, rgba(5,5,5,0) 45%, var(--wrap-black) 100%),
      linear-gradient(180deg, var(--photo-sky) 0%, var(--photo-wood) 25%, var(--photo-green) 55%, #2a2a2a 100%);
  }
  .service-list {
    position: absolute;
    left: 330px;
    top: 58px;
    list-style: none;
  }
  .service-list li {
    color: var(--gold);
    font-weight: 600;
    font-size: 28px;
    letter-spacing: 0.5px;
    line-height: 34px;
    display: flex;
    align-items: center;
  }
  .service-list li::before {
    content: "";
    width: 7px;
    height: 7px;
    background: #ffffff;
    margin-right: 14px;
  }
  .phone-banner {
    position: absolute;
    left: 240px;
    top: 210px;
    width: 360px;
    height: 72px;
  }
  .phone-banner svg { position: absolute; inset: 0; }
  .phone-number {
    position: absolute;
    left: 52px;
    top: 0;
    line-height: 72px;
    font-weight: 700;
    font-size: 34px;
    color: var(--ink);
    letter-spacing: 0.5px;
  }
  .brand-name {
    position: absolute;
    left: 668px;
    top: 236px;
    text-align: center;
    color: var(--gold);
    font-weight: 600;
    font-size: 14px;
    letter-spacing: 2px;
    line-height: 22px;
  }
</style>
</head>
<body>
  <div class="wrap-panel">
    <div class="home-photo" role="img" aria-label="Photo of a home under construction with timber framing and a lift"></div>

    <ul class="service-list">
      <li>CUSTOM HOMES</li>
      <li>REMODELS</li>
      <li>PAINTINGS</li>
      <li>COMMERCIAL</li>
    </ul>

    <div class="phone-banner">
      <svg width="360" height="72" viewBox="0 0 360 72" aria-hidden="true">
        <defs>
          <linearGradient id="gold-fade" x1="0" x2="1" y1="0" y2="0">
            <stop offset="0" stop-color="#d9c48f" stop-opacity="0"/>
            <stop offset="0.15" stop-color="#c9b27a"/>
            <stop offset="0.6" stop-color="#ece0b8"/>
            <stop offset="1" stop-color="#d9c48f"/>
          </linearGradient>
        </defs>
        <polygon points="0,0 325,0 360,36 325,72 0,72" fill="url(#gold-fade)"/>
      </svg>
      <span class="phone-number">816.555.0142</span>
    </div>

    <div class="brand-name">BRANTLEY<br>CONSTRUCTION</div>
  </div>
</body>
</html>
```